AV & Engineering company needs a Business Card Design

Like the simple design, don't too colorful. Smart & professional feel

Industry/Entity Type

Business

Requirements
Nice to have
• I would like to see the vertical design.

```html
<!DOCTYPE html>
<html lang="en">
<head>
<meta charset="utf-8">
<title>K&amp;R Signal Works Ltd – Business Card</title>
<link href="https://fonts.googleapis.com/css2?family=Arimo:wght@400;700&display=swap" rel="stylesheet">
<style>
  :root {
    --brand-red: #a3191f;
    --brand-red-dark: #8c1419;
    --card-white: #ffffff;
    --ink: #2b2b2b;
    --ink-soft: #555555;
    --backdrop: #ecebe8;
  }
  * { box-sizing: border-box; margin: 0; padding: 0; }
  html, body {
    width: 1200px; height: 840px; overflow: hidden;
    background: var(--backdrop);
    font-family: "Arimo", Arial, sans-serif;
  }
  .canvas {
    width: 1200px; height: 840px;
    display: flex; align-items: center; justify-content: center; gap: 80px;
  }
  .card {
    width: 360px; height: 630px; position: relative;
    box-shadow: 0 6px 24px rgba(0,0,0,0.12);
  }

  /* Front */
  .card-front { background: var(--card-white); }
  .frame-outer {
    position: absolute; inset: 10px;
    border: 9px solid var(--brand-red);
  }
  .frame-inner {
    position: absolute; inset: 26px;
    border: 2px solid var(--brand-red);
  }
  .front-brand {
    position: absolute; top: 158px; left: 40px; right: 30px;
    display: flex; align-items: center; gap: 10px;
  }
  .brand-square {
    width: 34px; height: 34px; background: var(--brand-red); flex: none;
  }
  .brand-name {
    color: var(--brand-red); font-weight: 700; line-height: 1.05;
  }
  .brand-name .line-1 { display: block; font-size: 31px; letter-spacing: 0.5px; }
  .brand-name .line-2 { display: block; font-size: 18px; letter-spacing: 4.5px; }

  .person {
    position: absolute; top: 390px; left: 44px;
  }
  .person-name { color: var(--brand-red); font-size: 17px; }
  .person-role { color: var(--ink); font-size: 12px; margin-top: 3px; }

  .contact-list {
    position: absolute; top: 448px; left: 44px; right: 30px;
    list-style: none;
  }
  .contact-list li {
    display: flex; align-items: flex-start; gap: 5px;
    font-size: 13.5px; color: var(--ink); line-height: 19px;
  }
  .contact-icon { width: 14px; height: 14px; flex: none; margin-top: 2px; fill: var(--brand-red); }

  /* Back */
  .card-back {
    background: linear-gradient(160deg, var(--brand-red) 0%, var(--brand-red-dark) 100%);
  }
  .back-brand {
    position: absolute; top: 260px; left: 0; right: 0;
    display: flex; align-items: center; justify-content: center; gap: 10px;
  }
  .card-back .brand-square { background: var(--card-white); }
  .card-back .brand-name { color: var(--card-white); }
</style>
</head>
<body>
<main class="canvas">

  <section class="card card-front" aria-label="Business card front">
    <div class="frame-outer"></div>
    <div class="frame-inner"></div>

    <div class="front-brand">
      <span class="brand-square"></span>
      <h1 class="brand-name">
        <span class="line-1">K&amp;R SIGNAL</span>
        <span class="line-2">WORKS LTD</span>
      </h1>
    </div>

    <div class="person">
      <p class="person-name">Dana Merrick</p>
      <p class="person-role">Owner/Operator</p>
    </div>

    <ul class="contact-list">
      <li>
        <svg class="contact-icon" viewBox="0 0 16 16"><rect x="4" y="1" width="8" height="14" rx="1.5"/><rect x="5.5" y="3" width="5" height="8" fill="#fff"/></svg>
        555-210-4417
      </li>
      <li>
        <svg class="contact-icon" viewBox="0 0 16 16"><path d="M3 1l3 3-1.5 2a9 9 0 0 0 5.5 5.5L12 10l3 3-2 2C7 15 1 9 1 3z"/></svg>
        555-210-4462
      </li>
      <li>
        <svg class="contact-icon" viewBox="0 0 16 16"><rect x="1" y="6" width="14" height="9" rx="1.5"/><path d="M3 6V3h10v3z"/><rect x="4" y="9" width="8" height="3" fill="#fff"/></svg>
        555-210-4490
      </li>
      <li>
        <svg class="contact-icon" viewBox="0 0 16 16"><rect x="1" y="3" width="14" height="10" rx="1.5"/><path d="M2 4l6 5 6-5" fill="none" stroke="#fff" stroke-width="1.5"/></svg>
        info@krsignalworks.com
      </li>
      <li>
        <svg class="contact-icon" viewBox="0 0 16 16"><circle cx="8" cy="8" r="7"/><path d="M1 8h14M8 1c-3 3.5-3 10.5 0 14M8 1c3 3.5 3 10.5 0 14" fill="none" stroke="#fff" stroke-width="1.1"/></svg>
        www.krsignalworks.com
      </li>
      <li>
        <svg class="contact-icon" viewBox="0 0 16 16"><path d="M8 1l7 6.5h-2V15H9.5v-4h-3v4H3V7.5H1z"/></svg>
        <span>4820 N. Ridgeview Road,<br>Elmford, CO 80417</span>
      </li>
    </ul>
  </section>

  <section class="card card-back" aria-label="Business card back">
    <div class="back-brand">
      <span class="brand-square"></span>
      <p class="brand-name">
        <span class="line-1">K&amp;R SIGNAL</span>
        <span class="line-2">WORKS LTD</span>
      </p>
    </div>
  </section>

</main>
</body>
</html>
```